Meadowbrook Foundation Brochure

We are looking for a new brochure design for our foundation. The foundation is a nonprofit organization that provides assistance to special needs families in Indiana. We do this by providing ipads, communication software, gas cards, and financial assistance to families for their special needs child.

Target Market(s)

Families

Industry/Entity Type

Foundation

Colors
0355a3
3176b5
34a6d7
9bcb3b

Requirements
Must have
• Clear concise information

```html
<!DOCTYPE html>
<html lang="en">
<head>
<meta charset="utf-8">
<title>Meadowbrook Foundation Brochure</title>
<link rel="stylesheet" href="https://fonts.googleapis.com/css2?family=Cinzel:wght@700;900&family=Roboto+Condensed:wght@400;700&display=swap">
<style>
  :root {
    --navy: #0355a3;
    --blue: #3176b5;
    --sky: #34a6d7;
    --green: #9bcb3b;
    --white: #ffffff;
    --ink: #1d1d1d;
    --page: #eef0f2;
  }
  * { box-sizing: border-box; margin: 0; padding: 0; }
  html, body { width: 1200px; height: 800px; overflow: hidden; background: var(--page); }
  .brochure {
    position: absolute; left: 105px; top: 17px;
    width: 990px; height: 766px; background: var(--white);
    box-shadow: 0 4px 18px rgba(0,0,0,.18);
    font-family: "Roboto Condensed", Arial, sans-serif;
    overflow: hidden;
  }
  .panel { position: absolute; top: 0; width: 330px; height: 766px; overflow: hidden; }
  .panel-left { left: 0; }
  .panel-middle { left: 330px; background: var(--green); }
  .panel-right { left: 660px; }

  .photo { position: absolute; }
  .photo-study { left: 0; top: 0; width: 330px; height: 320px;
    background: linear-gradient(160deg, #dfe6ec 0%, #9aa3ab 45%, #5b4e48 100%); }
  .what-we-do-art { position: absolute; left: 0; top: 270px; width: 330px; height: 310px; }
  .what-we-do { position: absolute; left: 30px; top: 300px; width: 285px; }
  .section-title {
    font-family: "Cinzel", Georgia, serif; font-weight: 700;
    color: var(--navy); font-size: 22px; letter-spacing: .5px; margin-bottom: 6px;
  }
  .body-text { font-size: 13.4px; line-height: 1.28; color: var(--ink); text-align: justify; }
  .body-text strong { font-weight: 700; }

  .photo-group { left: 0; top: 575px; width: 660px; height: 191px;
    background: linear-gradient(180deg, #8a8a55 0%, #5f7a3a 55%, #4f8a32 100%); }
  .group-band { position: absolute; left: 330px; top: 566px; width: 330px; height: 9px; background: var(--blue); }

  .top-band { position: absolute; left: 0; top: 0; width: 330px; height: 34px;
    background: linear-gradient(90deg, var(--navy), var(--sky)); }
  .logo-card {
    position: absolute; left: 85px; top: 70px; width: 160px; height: 160px;
    background: var(--white); border-radius: 14px;
    display: flex; flex-direction: column; align-items: center; justify-content: center; gap: 12px;
  }
  .logo-dot { width: 46px; height: 46px; border-radius: 50%; background: var(--navy); }
  .logo-name { font-weight: 700; color: var(--navy); font-size: 18px; text-align: center; line-height: 1.1; }
  .contact { position: absolute; left: 0; top: 268px; width: 330px; text-align: center; color: var(--navy); }
  .contact h2 { font-family: "Cinzel", Georgia, serif; font-weight: 700; font-size: 22px; margin-bottom: 6px; }
  .contact p { font-size: 17px; font-weight: 700; line-height: 1.2; }
  .contact .phone { font-size: 25px; margin-top: 30px; }
  .contact .web { margin-top: 22px; font-size: 19px; }

  .photo-swing { left: 0; top: 0; width: 330px; height: 500px;
    background: linear-gradient(170deg, #3f6a3a 0%, #2c3b2c 40%, #8c2a2a 70%, #2b3650 100%); }
  .swing-curve { position: absolute; left: 0; top: 410px; width: 330px; height: 130px; }
  .headline {
    position: absolute; left: 0; top: 575px; width: 330px; text-align: center;
    font-family: "Cinzel", Georgia, serif; font-weight: 900; color: var(--navy);
    font-size: 29px; line-height: 1.08;
  }
  .foot-band { position: absolute; left: 0; top: 742px; width: 330px; height: 12px; background: var(--green); }
</style>
</head>
<body>
<main class="brochure">
  <section class="panel panel-left">
    <div class="photo photo-study" role="img" aria-label="Photo of two young people working together at a table"></div>
    <svg class="what-we-do-art" viewBox="0 0 330 310" aria-hidden="true">
      <rect x="0" y="0" width="330" height="310" fill="var(--navy)"/>
      <path d="M0 40 Q150 10 330 30 L330 310 L0 310 Z" fill="var(--blue)"/>
      <path d="M0 22 Q160 -4 330 12 L330 280 Q300 306 200 306 Q30 306 0 270 Z" fill="var(--green)"/>
      <path d="M8 28 Q170 4 330 20 L330 262 Q300 292 200 294 Q40 294 8 262 Z" fill="var(--white)"/>
    </svg>
    <div class="what-we-do">
      <h2 class="section-title">What We Do</h2>
      <p class="body-text"><strong>“The Meadowbrook Foundation</strong> provides assistance to special needs families – in whatever way they may need it. For some families that is easing the financial burden of therapy, for others it is providing a tablet and language software so their nonverbal child can communicate. For others, it may mean providing diapers or clothing or gas cards to drive their children to doctor’s appointments. We understand that each family is unique and that means assisting them in different ways, and we are to do that.</p>
    </div>
  </section>

  <section class="panel panel-middle">
    <div class="top-band"></div>
    <div class="logo-card">
      <span class="logo-dot"></span>
      <span class="logo-name">Meadowbrook<br>Foundation</span>
    </div>
    <div class="contact">
      <h2>Contact Us</h2>
      <p>Meadowbrook Foundation</p>
      <p>1240 Willow Creek Drive</p>
      <p>Elkhart, IN 46514</p>
      <p class="phone">574-555-0142</p>
      <p class="web">www.meadowbrookfdn.org<br>info@meadowbrookfdn.org</p>
    </div>
  </section>

  <div class="group-band"></div>
  <div class="photo photo-group" role="img" aria-label="Group photo of volunteers and children standing together outdoors on grass"></div>

  <section class="panel panel-right">
    <div class="photo photo-swing" role="img" aria-label="Photo of a smiling boy on a playground swing"></div>
    <svg class="swing-curve" viewBox="0 0 330 130" aria-hidden="true">
      <path d="M0 0 Q60 95 190 100 Q280 100 330 70 L330 130 L0 130 Z" fill="var(--navy)"/>
      <path d="M0 14 Q70 108 200 110 Q285 110 330 82 L330 130 L0 130 Z" fill="var(--green)"/>
      <path d="M0 26 Q80 118 205 120 Q290 120 330 94 L330 130 L0 130 Z" fill="var(--white)"/>
    </svg>
    <h1 class="headline">Providing<br>Hope for<br>Special Needs<br>Families</h1>
    <div class="foot-band"></div>
  </section>
</main>
</body>
</html>
```